Stationery Design for Consulting Company
Orvel Partners
Creative Brief
Professional
Tomas Wenholt
Director
Orvel Partners LLC 48215 Ridgefern Road Dunmore, DE 19872 USA
tomas@orvel-advisory.com
www.orvel-advisory.com
Maybe just a larger logo in the middle unless you have better ideas. I'm open to suggestions.

```html
<!DOCTYPE html>
<html lang="en">
<head>
<meta charset="utf-8">
<title>Orvel Partners – Business Card</title>
<link rel="stylesheet" href="https://fonts.googleapis.com/css2?family=Montserrat:wght@400;600;700&display=swap">
<style>
  :root {
    --backdrop: #d9d9d9;
    --card-dark: #2a2a2b;
    --card-light: #ffffff;
    --accent: #f5a623;
    --text-light: #ffffff;
    --text-muted: #bdbdbd;
    --text-dark: #4a4a4a;
    --icon: #7a7a7a;
  }
  html, body {
    margin: 0;
    width: 1200px;
    height: 653px;
    overflow: hidden;
    background: var(--backdrop);
    font-family: "Montserrat", sans-serif;
  }
  .stage {
    position: relative;
    width: 1200px;
    height: 653px;
  }
  .card {
    position: absolute;
    top: 183px;
    width: 500px;
    height: 286px;
    overflow: hidden;
    box-shadow: 0 6px 18px rgba(0,0,0,0.25);
  }
  .card--front { left: 70px; background: var(--card-dark); }
  .card--back { left: 630px; background: var(--card-dark); }

  .brand {
    text-align: center;
  }
  .brand__name {
    color: var(--accent);
    font-weight: 700;
    letter-spacing: 0.02em;
    margin: 0;
    line-height: 1.1;
  }
  .brand__tagline {
    margin: 6px 0 0;
    font-size: 7px;
    letter-spacing: 0.14em;
    text-transform: uppercase;
  }

  .card--front .brand {
    position: absolute;
    left: 0; right: 0;
    top: 108px;
  }
  .card--front .brand__name { font-size: 34px; }
  .card--front .brand__tagline { color: var(--text-muted); }

  .back-shape { position: absolute; inset: 0; }

  .card--back .brand {
    position: absolute;
    right: 28px;
    top: 30px;
    text-align: right;
  }
  .card--back .brand__name { font-size: 24px; }
  .card--back .brand__tagline { color: var(--text-dark); font-size: 6px; }

  .contact {
    position: absolute;
    right: 28px;
    top: 108px;
    margin: 0;
    padding: 0;
    list-style: none;
    text-align: right;
    font-size: 8px;
    color: var(--text-dark);
    line-height: 1.5;
  }
  .contact__address { margin-bottom: 10px; }
  .contact__item {
    display: flex;
    justify-content: flex-end;
    align-items: center;
    gap: 6px;
    margin-bottom: 3px;
  }
  .contact__icon { width: 8px; height: 8px; fill: var(--icon); }

  .holder {
    position: absolute;
    left: 34px;
    bottom: 24px;
    margin: 0;
    color: var(--text-light);
    font-size: 11px;
    font-weight: 600;
    letter-spacing: 0.08em;
    text-transform: uppercase;
  }
</style>
</head>
<body>
<main class="stage">
  <section class="card card--front" aria-label="Card front">
    <div class="brand">
      <p class="brand__name">Orvel Partners LLC</p>
      <p class="brand__tagline">Consulting Strategy &amp; Management</p>
    </div>
  </section>

  <section class="card card--back" aria-label="Card back">
    <svg class="back-shape" viewBox="0 0 500 286" preserveAspectRatio="none" aria-hidden="true">
      <path d="M62 0 H500 V286 H300 C150 272 42 182 62 0 Z" fill="var(--card-light)"/>
      <path d="M54 0 C36 176 144 270 292 286" fill="none" stroke="var(--accent)" stroke-width="7"/>
    </svg>

    <div class="brand">
      <p class="brand__name">Orvel Partners LLC</p>
      <p class="brand__tagline">Consulting Strategy &amp; Management</p>
    </div>

    <ul class="contact">
      <li class="contact__address">48215 Ridgefern Road<br>Dunmore, DE 19872 USA</li>
      <li class="contact__item">302 555 0148
        <svg class="contact__icon" viewBox="0 0 10 10"><path d="M2 0.5 L4 2.8 L3 4 C3.6 5.4 4.6 6.4 6 7 L7.2 6 L9.5 8 L8.2 9.5 C4 9 1 6 0.5 1.8 Z"/></svg>
      </li>
      <li class="contact__item">302 555 0193
        <svg class="contact__icon" viewBox="0 0 10 10"><path d="M2 0.5 L4 2.8 L3 4 C3.6 5.4 4.6 6.4 6 7 L7.2 6 L9.5 8 L8.2 9.5 C4 9 1 6 0.5 1.8 Z"/></svg>
      </li>
      <li class="contact__item">302 555 0176
        <svg class="contact__icon" viewBox="0 0 10 10"><rect x="2" y="0.5" width="6" height="9" rx="1"/></svg>
      </li>
      <li class="contact__item">tomas@orvel-advisory.com
        <svg class="contact__icon" viewBox="0 0 10 10"><path d="M0 2 H10 V8 H0 Z M0 2 L5 5.5 L10 2" /></svg>
      </li>
      <li class="contact__item">www.orvel-advisory.com
        <svg class="contact__icon" viewBox="0 0 10 10"><circle cx="5" cy="5" r="4.5"/></svg>
      </li>
    </ul>

    <p class="holder">Tomas Wenholt</p>
  </section>
</main>
</body>
</html>
```